Covid19 Poster for workplaces

Create a poster on how to protect yourself from Corona virus at work.
We are a Teamwell Haven company. We have just re-branded so we need to fit in with our brand. We like clean and fresh, slightly amusing is ok if it will draw attention but it's an important topic. A4 and A3 please.

Content:

Headline: Lower the risk of COVID 19 in the workplace.

BE WELL

Bring your own cup - don’t share cups and food.
Elbow tap instead of handshakes and kisses
Wash your hands often - with soap.
Elbow or tissues when you cough or sneeze then straight in the bin
Leave your face alone after touching shared surfaces
Leave your bugs at home if you’re feeling unwell.

Call health line if you have a cough, a high temperature and shortness of breath. 0800 472 9160

Based on recommendations from ZPK and QLN

Target Market(s)

Employees - so anyone

Other font styles liked:
• Use the closest font to the brand documents

Requirements
Should not have
• Clip art

```html
<!DOCTYPE html>
<html lang="en">
<head>
<meta charset="utf-8">
<title>Lower the risk of COVID 19 in the Workplace</title>
<link href="https://fonts.googleapis.com/css2?family=Arimo:wght@700&display=swap" rel="stylesheet">
<style>
  :root {
    --teal: #1eabb6;
    --teal-dark: #0e2a3d;
    --navy: #0a1f30;
    --green: #8cc63f;
    --ink: #2b2b2b;
    --white: #ffffff;
    --band: #e6e6e6;
    --dash: #9a9a9a;
  }
  * { margin: 0; padding: 0; box-sizing: border-box; }
  html, body { width: 926px; height: 1200px; overflow: hidden; background: var(--white); }
  body { font-family: "Arimo", Arial, sans-serif; font-weight: 700; color: var(--ink); }
  .poster { position: relative; width: 926px; height: 1200px; background: var(--white); overflow: hidden; }

  .hero { position: absolute; left: 0; top: 0; width: 926px; height: 367px; background: var(--teal); }
  .brand { position: absolute; left: 48px; top: 58px; display: flex; align-items: center; gap: 12px; }
  .brand-dot { width: 34px; height: 34px; border-radius: 50%; background: var(--white); }
  .brand-name { font-size: 30px; line-height: 32px; color: var(--navy); }
  .headline { position: absolute; left: 48px; top: 200px; font-size: 42px; line-height: 45px; color: var(--white); letter-spacing: -0.3px; }
  .hero-art { position: absolute; left: 425px; top: 39px; width: 501px; height: 298px; border-radius: 150px 0 0 150px;
    background: radial-gradient(circle at 35% 55%, #2f5d78 0%, #123049 40%, var(--navy) 80%); }

  .band { position: absolute; height: 148px; }
  .band-right { left: 479px; width: 447px; background: linear-gradient(90deg, var(--white), var(--band)); }
  .band-left { left: 0; width: 412px; background: linear-gradient(90deg, var(--band), var(--white)); }

  .tip-icon { position: absolute; width: 112px; height: 112px; border-radius: 50%; border: 4px solid; background: var(--white); }
  .tip-icon::after { content: ""; position: absolute; inset: 5px; border-radius: 50%; background: currentColor; }
  .tip-icon.green { color: var(--green); border-color: var(--green); }
  .tip-icon.teal { color: var(--teal); border-color: var(--teal); }

  .tip-text { position: absolute; font-size: 21px; line-height: 26px; color: var(--ink); }

  .call-box { position: absolute; left: 176px; top: 932px; width: 670px; height: 159px; border: 1.5px dashed var(--dash); border-radius: 14px; }
  .call-text { position: absolute; left: 0; right: 0; top: 16px; text-align: center; font-size: 24px; line-height: 27px; color: var(--ink); }
  .call-number { position: absolute; left: 0; right: 0; top: 68px; text-align: center; font-size: 70px; line-height: 72px; color: var(--green); letter-spacing: -2px; }
  .call-icon { position: absolute; left: 56px; top: 955px; width: 112px; height: 112px; border-radius: 50%; border: 4px solid var(--green); background: var(--white); }
  .call-icon svg { position: absolute; inset: 5px; }

  .source { position: absolute; left: 0; top: 1137px; width: 716px; height: 48px; background: var(--teal); border-radius: 0 24px 24px 0;
    color: var(--white); font-size: 23px; line-height: 48px; padding-left: 48px; }
  .partner-badge { position: absolute; top: 1122px; }
  .partner-round { left: 756px; width: 70px; height: 70px; border-radius: 50%; background: #3c6eb4; }
  .partner-oval { left: 853px; width: 36px; height: 66px; border-radius: 18px; background: #e24b3b; border: 3px solid #8cc63f; }
</style>
</head>
<body>
<main class="poster">
  <header class="hero">
    <div class="brand"><span class="brand-dot"></span><span class="brand-name">Teamwell<br>Haven</span></div>
    <h1 class="headline">Lower the risk of<br>COVID 19 in the<br>Workplace.</h1>
    <div class="hero-art" role="img" aria-label="Illustration of virus particles on a dark blue background"></div>
  </header>

  <div class="band band-right" style="top:395px"></div>
  <div class="band band-left" style="top:565px"></div>
  <div class="band band-right" style="top:743px"></div>

  <div class="tip-icon green" style="left:56px;top:411px" role="img" aria-label="Icon of a hand holding a cup"></div>
  <p class="tip-text" style="left:244px;top:444px">Bring your own cup -<br>don’t share cups and<br>food.</p>

  <div class="tip-icon teal" style="left:487px;top:411px" role="img" aria-label="Icon of two elbows tapping"></div>
  <p class="tip-text" style="left:604px;top:444px">Elbow tap instead<br>of Handshakes and<br>Kisses</p>

  <div class="tip-icon green" style="left:56px;top:580px" role="img" aria-label="Icon of hands washing with soap"></div>
  <p class="tip-text" style="left:244px;top:617px">Wash your Hands<br>Often - with soap.</p>

  <div class="tip-icon teal" style="left:487px;top:580px" role="img" aria-label="Icon of a hand dropping a tissue"></div>
  <p class="tip-text" style="left:604px;top:591px">Elbow or tissues<br>when you cough or<br>sneeze then straight<br>in the bin</p>

  <div class="tip-icon green" style="left:56px;top:763px" role="img" aria-label="Icon of a person with a hand near the face"></div>
  <p class="tip-text" style="left:244px;top:782px">Leave your face<br>alone after touching<br>shared surfaces</p>

  <div class="tip-icon teal" style="left:487px;top:763px" role="img" aria-label="Icon of a bug"></div>
  <p class="tip-text" style="left:604px;top:782px">Leave your bugs<br>at home if you’re<br>feeling unwell.</p>

  <section class="call-box">
    <p class="call-text">Call health line if you have a cough, a high<br>temperature and shortness of breath.</p>
    <p class="call-number">0800 472 9160</p>
  </section>
  <div class="call-icon">
    <svg viewBox="0 0 100 100" width="94" height="94" aria-hidden="true">
      <circle cx="50" cy="50" r="50" fill="#8cc63f"/>
      <path d="M33 28c-4 2-7 6-6 11 2 12 18 30 31 34 5 1 9-1 11-5l-9-9-6 4c-5-2-13-10-15-16l4-6z" fill="none" stroke="#fff" stroke-width="3.5" stroke-linejoin="round"/>
      <path d="M56 32a14 14 0 0 1 12 12M58 22a24 24 0 0 1 20 20" fill="none" stroke="#fff" stroke-width="3.5" stroke-linecap="round"/>
    </svg>
  </div>

  <footer>
    <p class="source">Based on recommendations from ZPK and QLN</p>
    <span class="partner-badge partner-round" aria-hidden="true"></span>
    <span class="partner-badge partner-oval" aria-hidden="true"></span>
  </footer>
</main>
</body>
</html>
```